Real Estate Open House A Frame Sign

The sign is 22" wide and 28" tall. This sign is used to post around the neighbourhood to direct people to an open house (home that is for sale). It is also used for self-promotion.

Designwise
- I just want something with a modern look, simple and clean.
- I want my picture and business logo on the left side.
- On the right side, website (www.lumwick-realestate.com) and my phone (555-374-9126), then a blank space where I can write an address when I need to.

I'm not sure how I want the overall design look. I'm very open-minded and I'm depending on your creative mind to come up with something.

If you have any questions, please let me know.

```html
<!DOCTYPE html>
<html lang="en">
<head>
<meta charset="utf-8">
<title>Lumwick Real Estate – Open House Signs</title>
<link rel="stylesheet" href="https://fonts.googleapis.com/css2?family=Lato:wght@400;700;900&display=swap">
<style>
  :root {
    --brand-blue: #0530a6;
    --paper: #ffffff;
    --suit-dark: #1b2230;
    --suit-mid: #2f3a4d;
    --shadow: rgba(0, 0, 0, 0.45);
  }
  html, body {
    margin: 0;
    padding: 0;
    width: 1200px;
    height: 1200px;
    overflow: hidden;
    background: var(--paper);
  }
  .canvas {
    position: relative;
    width: 1200px;
    height: 1200px;
  }
  .sign {
    position: absolute;
    display: block;
    filter: drop-shadow(-4px 4px 8px var(--shadow));
  }
  .sign--landscape { left: 72px;  top: 76px;  width: 528px; height: 416px; }
  .sign--portrait  { left: 106px; top: 549px; width: 462px; height: 587px; }
  .sign--band      { left: 664px; top: 298px; width: 444px; height: 564px; }

  .sign-bg { fill: var(--brand-blue); }
  .white-shape { fill: var(--paper); }
  .accent-line { stroke: var(--brand-blue); stroke-width: 1.5; fill: none; }

  .brand-name {
    font-family: "Lato", sans-serif;
    font-weight: 400;
    fill: var(--paper);
  }
  .brand-name .brand-sub { letter-spacing: 7px; }
  .headline {
    font-family: "Lato", sans-serif;
    font-weight: 900;
    fill: var(--brand-blue);
  }
  .phone {
    font-family: "Lato", sans-serif;
    font-weight: 900;
  }
  .phone--light { fill: var(--paper); }
  .phone--dark { fill: var(--brand-blue); }
  .website {
    font-family: "Lato", sans-serif;
    font-weight: 400;
    fill: var(--paper);
  }
</style>
</head>
<body>
<main class="canvas">

  <!-- Landscape sign -->
  <svg class="sign sign--landscape" viewBox="0 0 660 520" xmlns="http://www.w3.org/2000/svg">
    <defs>
      <linearGradient id="agentToneA" x1="0" y1="0" x2="0" y2="1">
        <stop offset="0" stop-color="#2f3a4d"/>
        <stop offset="1" stop-color="#161c28"/>
      </linearGradient>
    </defs>
    <rect class="sign-bg" width="660" height="520"/>
    <text class="brand-name" x="48" y="100" font-size="56">LUMWICK
      <tspan class="brand-sub" x="48" y="130" font-size="20">REAL ESTATE</tspan>
    </text>
    <path role="img" aria-label="Portrait photo of the agent in a dark suit, arms crossed"
          fill="url(#agentToneA)"
          d="M75 175 Q75 145 120 145 Q165 145 165 180 L170 280 Q235 300 252 380 L255 520 L10 520 L14 330 Q30 290 80 280 Z"/>
    <polygon class="white-shape" points="200,182 545,182 545,155 630,210 545,264 545,242 200,242"/>
    <text class="headline" x="212" y="230" font-size="50" font-weight="700">OPEN HOUSE</text>
    <text class="phone phone--light" x="203" y="335" font-size="58">555-374-9126</text>
    <text class="website" x="402" y="375" font-size="23" text-anchor="middle">www.lumwick-realestate.com</text>
  </svg>

  <!-- Portrait sign with wave -->
  <svg class="sign sign--portrait" viewBox="0 0 578 734" xmlns="http://www.w3.org/2000/svg">
    <defs>
      <linearGradient id="agentToneB" x1="0" y1="0" x2="0" y2="1">
        <stop offset="0" stop-color="#2f3a4d"/>
        <stop offset="1" stop-color="#161c28"/>
      </linearGradient>
    </defs>
    <rect class="sign-bg" width="578" height="734"/>
    <text class="website" x="62" y="72" font-size="24">www.lumwick-realestate.com</text>
    <polygon class="white-shape" points="46,87 430,87 430,50 552,124 430,196 430,167 46,167"/>
    <text class="headline" x="60" y="145" font-size="56">OPEN HOUSE</text>
    <path role="img" aria-label="Portrait photo of the agent in a dark suit, arms crossed"
          fill="url(#agentToneB)"
          d="M95 220 Q95 182 150 182 Q205 182 205 225 L208 340 Q290 370 308 460 L310 575 L14 585 L18 410 Q35 355 100 335 Z"/>
    <text class="brand-name" x="265" y="340" font-size="62">LUMWICK
      <tspan class="brand-sub" x="265" y="368" font-size="19">REAL ESTATE</tspan>
    </text>
    <path class="white-shape" d="M0 590 C120 540 220 575 330 602 C440 625 545 570 578 480 L578 734 L0 734 Z"/>
    <path d="M0 590 C120 540 220 575 330 602 C440 625 545 570 578 480" stroke="#c8cbd3" stroke-width="2" fill="none"/>
    <text class="phone phone--dark" x="289" y="682" font-size="64" text-anchor="middle">555-374-9126</text>
  </svg>

  <!-- Square sign with diagonal band -->
  <svg class="sign sign--band" viewBox="0 0 555 705" xmlns="http://www.w3.org/2000/svg">
    <defs>
      <linearGradient id="agentToneC" x1="0" y1="0" x2="0" y2="1">
        <stop offset="0" stop-color="#2f3a4d"/>
        <stop offset="1" stop-color="#161c28"/>
      </linearGradient>
    </defs>
    <rect class="sign-bg" width="555" height="705"/>
    <path role="img" aria-label="Portrait photo of the agent in a dark suit, arms crossed"
          fill="url(#agentToneC)"
          d="M58 60 Q58 18 112 18 Q168 18 168 62 L170 180 Q240 215 258 330 L262 400 L0 432 L0 205 Q30 180 60 172 Z"/>
    <text class="brand-name" x="225" y="150" font-size="68">LUMWICK
      <tspan class="brand-sub" x="225" y="181" font-size="21">REAL ESTATE</tspan>
    </text>
    <polygon class="white-shape" points="0,430 555,365 555,557 0,620"/>
    <line class="accent-line" x1="180" y1="410" x2="555" y2="367"/>
    <line class="accent-line" x1="65" y1="615" x2="555" y2="558"/>
    <g transform="rotate(-6.7 0 430)">
      <text class="website" x="55" y="398" font-size="28">www.lumwick-realestate.com</text>
      <text class="headline" x="20" y="515" font-size="68">OPEN HOUSE</text>
      <text class="phone phone--dark" x="80" y="590" font-size="56">555-374-9126</text>
    </g>
  </svg>

</main>
</body>
</html>
```